Reggie Vosburn - Free Personalised Health Consultation - "Every body walks its own path"

This flyer will be left on tables/seats at speaking events and seminars and used to attain leads.

Top half will have "SMS me for a FREE Personalised Health Consultation" and my picture (see www.reggievosburn.example and pick most engaging photo) and underneath my contact details. It must have lines with "Notes:" halfway down so people can take notes at the seminar and lines on the back with my contact details again and "Notes: with lines.

I am having a business card also being designed by Plotnest for same and would like the flyer and business card to carry a similar feel/look for consistency.

Below is the brief for the business card being designed:
Business Card for www.reggievosburn.example site. It is a trust site and I use it for 1:1 relatable connections. It is the one I use for building intimate 1:1 trust building and Exec Coaching Services and programs for high wealth individuals and corporates. I also have a commercial programmatic site of my personal health products and services and programs for main stream one to many. www.crossgenvitality.example that can also provoke thought for the www.reggievosburn.example business card. (mind you will get a separate business card for that site, but want to provide context). It has a logo which you may want to draw from in designing the reggievosburn business card which is personal and is about building my brand. There is also a reggievosburn personal KX page and reggievosburn business KX page. I am a Certified Talent Compass 4.1 Coach with Verrick and you can get a corporate brief of me on there to give you more context https://www.verricktalenthub.example/coach/en-us/directory?search=reggie

Target Market(s)

Exec, IT, Health conscious. Corporates wanting to run Health and Wellness programs. Those wanting to go from good to great. Millennials to Middleaged.

Industry/Entity Type

Health And Wellness

Font styles to use
Sans Serif
Other font styles liked:
• Arial and Calibri ok too

Colors

Designer to choose colors to be used in the design.

Requirements
Must have
• Picture of me - use best from www.reggievosburn.example or can send one you choose.
• Contact details like my buisness card being designed by you guys in separate project.
• Name: Reggie Vosburn
• email: reggie@reggievosburn.,example
• Phone: Australia +61 455 318 026 Singapore: +65 8342 1960
Nice to have
• Open to ideas

```html
<!DOCTYPE html>
<html lang="en">
<head>
<meta charset="utf-8">
<title>Reggie Vosburn – Notes</title>
<link rel="stylesheet" href="https://fonts.googleapis.com/css2?family=Montserrat:wght@700&family=Roboto:wght@300;400&display=swap">
<style>
  :root {
    --ink-dark: #1e1e1e;
    --footer-dark: #2b2929;
    --paper: #f6f6f6;
    --rule: #c9c9c9;
    --tab: #c0c0c0;
    --tab-fold: #8c8c8c;
    --divider: #e6e6e6;
    --light-text: #ececec;
    --white: #ffffff;
  }
  * { margin: 0; padding: 0; box-sizing: border-box; }
  html, body { width: 848px; height: 1200px; overflow: hidden; }
  body { font-family: "Roboto", Arial, sans-serif; background: var(--paper); }

  .notepad { position: relative; width: 848px; height: 1200px; background: var(--paper); overflow: hidden; }

  .header-band { position: absolute; left: 0; top: 0; width: 848px; height: 117px; background: var(--ink-dark); }
  .brand-name {
    position: absolute; left: 0; top: 48px; width: 848px; text-align: center;
    color: var(--white); font-weight: 300; font-size: 40px; letter-spacing: 1px; line-height: 1;
  }

  .notes-tab { position: absolute; left: 224px; top: 106px; width: 400px; height: 46px; }
  .notes-label {
    position: absolute; left: 224px; top: 116px; width: 400px; text-align: center;
    color: var(--white); font-family: "Montserrat", Arial, sans-serif; font-weight: 700;
    font-size: 22px; letter-spacing: 0.3px; line-height: 28px;
  }

  .ruled-lines { position: absolute; left: 52px; top: 203px; width: 743px; }
  .ruled-lines .rule { height: 49.8px; border-top: 1.5px solid var(--rule); }

  .footer-divider { position: absolute; left: 0; top: 1047px; width: 848px; height: 7px; background: var(--divider); }
  .contact-footer { position: absolute; left: 0; top: 1054px; width: 848px; height: 146px; background: var(--footer-dark); color: var(--light-text); }

  .contact-icon { position: absolute; width: 24px; height: 24px; }
  .contact-text { position: absolute; font-size: 19px; font-weight: 400; line-height: 24px; white-space: nowrap; }
</style>
</head>
<body>
<main class="notepad">
  <header class="header-band">
    <h1 class="brand-name">Reggie Vosburn</h1>
  </header>

  <svg class="notes-tab" viewBox="0 0 400 46" aria-hidden="true">
    <polygon points="2,0 12,0 12,10" fill="var(--tab-fold)"/>
    <polygon points="398,0 388,0 388,10" fill="var(--tab-fold)"/>
    <polygon points="8,2 392,2 378,45 22,45" fill="var(--tab)"/>
  </svg>
  <div class="notes-label">NOTES</div>

  <section class="ruled-lines" aria-label="Note lines">
    <div class="rule"></div><div class="rule"></div><div class="rule"></div><div class="rule"></div>
    <div class="rule"></div><div class="rule"></div><div class="rule"></div><div class="rule"></div>
    <div class="rule"></div><div class="rule"></div><div class="rule"></div><div class="rule"></div>
    <div class="rule"></div><div class="rule"></div><div class="rule"></div><div class="rule"></div>
    <div class="rule"></div>
  </section>

  <div class="footer-divider"></div>
  <footer class="contact-footer">
    <svg class="contact-icon" style="left:49px;top:24px" viewBox="0 0 24 24" aria-hidden="true">
      <path d="M6 3c1 0 2 .5 2 1.5v3c0 1-1 1.3-1.6 1.6.4 2.2 1.4 4 3 5.3.5-.5 1-1.3 2-1.1l2.6.8c.9.3 1 1.2 1 2v2.4c0 1-1 1.5-2 1.5C7 20 3 14 3 6c0-1.5 1.5-3 3-3z" fill="var(--white)"/>
      <path d="M16 8a4 4 0 0 1 0 6M18.5 6a7 7 0 0 1 0 10" stroke="var(--white)" stroke-width="1.6" fill="none" stroke-linecap="round"/>
    </svg>
    <div class="contact-text" style="left:97px;top:17px">Australia: +61 455 318 026</div>
    <div class="contact-text" style="left:97px;top:41px">Singapore: +65 8342 1960</div>

    <svg class="contact-icon" style="left:416px;top:19px" viewBox="0 0 24 24" aria-hidden="true">
      <circle cx="12" cy="12" r="4" stroke="var(--white)" stroke-width="2.6" fill="none"/>
      <path d="M16 8v5.5c0 1.8 3.5 1.8 3.5-1.5A7.5 7.5 0 1 0 15 19" stroke="var(--white)" stroke-width="2.6" fill="none" stroke-linecap="round"/>
    </svg>
    <div class="contact-text" style="left:464px;top:19px">reggie@reggievosburn.,example</div>

    <svg class="contact-icon" style="left:416px;top:48px" viewBox="0 0 24 24" aria-hidden="true">
      <circle cx="12" cy="12" r="9" stroke="var(--white)" stroke-width="2" fill="none"/>
      <path d="M3 12h18M12 3c-3 3-3 15 0 18M12 3c3 3 3 15 0 18M5 7h14M5 17h14" stroke="var(--white)" stroke-width="1.6" fill="none"/>
    </svg>
    <div class="contact-text" style="left:464px;top:47px">www.reggievosburn.example</div>

    <svg class="contact-icon" style="left:416px;top:77px" viewBox="0 0 24 24" aria-hidden="true">
      <path d="M12 2a7.5 7.5 0 0 0-7.5 7.5C4.5 15 12 22 12 22s7.5-7 7.5-12.5A7.5 7.5 0 0 0 12 2z" fill="var(--white)"/>
      <circle cx="12" cy="9.5" r="2.8" fill="var(--footer-dark)"/>
    </svg>
    <div class="contact-text" style="left:464px;top:76px">Your Address goes here</div>
  </footer>
</main>
</body>
</html>
```